Motor Vault Website - Part of the Brantley Group

A complimentary website is required for the launch of a 'Motor Vault' - a new service launched by industry renowned BRANTLEY. Motor Vault is an industry-first brand that designs and builds unique subterranean car parks for private residential homes in London and the influential counties within the UK. Please see here the direction of a new BRANTLEY Website - we would like Motor Vault to be complimentary and sit alongside BRANTLEY harmoniously - https://www.brantleyhq.example/brantley-nu-staging Brantley have some images, but whilst more professional images are in production - we have also attached pixmoor photos- named clearly as pixmoor. **Attached files include JPEG, .eps of logo and Brantley library images and Pixmoor Library Images - two versions of logo dependent on background colour. - Website needs to be sleek, chic and masculine.- Colour Palette - Grey/ Black/ White - Same visiual journey as Brantley website- Required areas within the sit include - About Us / Our Work / Contact Page

Target Market(s)

Luxury
Men

Number of Pages Required

2 page

Font styles to use
Sans Serif

Colors
e8e8e8
757575
1b1b1b
000000
9d9d9d
cbcbcb
f5f5f5

Requirements
Must have
• Complimentary of this site - https://www.brantleyhq.example/brantley-nu-staging
Should not have
• Colour

```html
<!DOCTYPE html>
<html lang="en">
<head>
<meta charset="utf-8">
<title>Motor Vault</title>
<link href="https://fonts.googleapis.com/css2?family=Lato:ital,wght@0,400;0,700;0,900;1,700&family=Montserrat:wght@600;700&display=swap" rel="stylesheet">
<style>
:root{
  --white:#ffffff;
  --paper:#f5f5f5;
  --band:#e8e8e8;
  --line:#cbcbcb;
  --mid:#9d9d9d;
  --grey:#757575;
  --ink:#1b1b1b;
  --black:#000000;
  --social-a:#3b5998;
  --social-b:#0e76a8;
  --social-c:#1da1f2;
  --social-d:#dd4b39;
}
*{margin:0;padding:0;box-sizing:border-box}
html,body{width:1200px;height:2995px;overflow:hidden}
body{position:relative;background:var(--white);font-family:'Lato',sans-serif;color:var(--ink)}

/* hero */
.hero{position:absolute;left:0;top:0;width:1200px;height:695px;
  clip-path:polygon(0 0,1200px 0,1200px 598px,600px 695px,0 598px);
  background:
    linear-gradient(105deg,rgba(255,255,255,0) 36%,rgba(255,255,255,.16) 40%,rgba(255,255,255,0) 46%),
    linear-gradient(75deg,rgba(255,255,255,0) 28%,rgba(255,255,255,.10) 31%,rgba(255,255,255,0) 35%),
    radial-gradient(ellipse 160px 120px at 1010px 190px,rgba(230,230,230,.55) 0%,rgba(230,230,230,0) 100%),
    radial-gradient(ellipse 300px 260px at 700px 240px,rgba(140,140,140,.55) 0%,rgba(60,60,60,0) 100%),
    linear-gradient(160deg,#3a3a3a 0%,#242424 40%,#171717 75%,#0d0d0d 100%)}
.hero::after{content:"";position:absolute;inset:0;background:linear-gradient(180deg,rgba(0,0,0,.25) 0%,rgba(0,0,0,0) 25%,rgba(0,0,0,0) 70%,rgba(0,0,0,.35) 100%)}
.brand{position:absolute;font-family:'Lato',sans-serif;font-weight:900;letter-spacing:1px;white-space:nowrap;display:flex;align-items:center;gap:10px;z-index:2}
.brand .mark{display:inline-block;background:currentColor}
.hero .brand{left:120px;top:12px;color:var(--white);font-size:38px}
.hero .brand .mark{width:24px;height:24px}
.nav{position:absolute;top:28px;left:586px;display:flex;align-items:center;color:var(--white);font-weight:700;font-size:16px;z-index:2}
.nav a{color:inherit;text-decoration:none;padding:0 21px;position:relative}
.nav a+a{border-left:1px solid rgba(255,255,255,.55)}
.nav .current::before{content:"";position:absolute;left:0;top:-8px;width:70px;height:16px;border-top:5px solid var(--mid);border-left:5px solid var(--mid)}
.nav .current::after{content:"";position:absolute;right:-2px;bottom:-10px;width:30px;height:14px;border-bottom:5px solid var(--mid);border-right:5px solid var(--mid)}
.hero-title{position:absolute;top:306px;left:0;width:1200px;text-align:center;color:var(--white);font-family:'Montserrat',sans-serif;font-weight:700;font-size:24px;line-height:37px;letter-spacing:1.5px;text-transform:uppercase;z-index:2}
.dots{position:absolute;top:636px;left:548px;display:flex;gap:16px;z-index:2}
.dots span{width:12px;height:12px;border-radius:50%;background:var(--white)}
.dots span.on{background:transparent;border:2px solid var(--white)}

/* section titles */
.section-title{position:absolute;font-family:'Lato',sans-serif;font-weight:700;font-size:31px;color:var(--ink);letter-spacing:.5px;text-transform:uppercase}
.framed{padding:14px 12px 6px}
.framed::before{content:"";position:absolute;left:0;top:0;width:44px;height:46px;border-top:6px solid var(--grey);border-left:6px solid var(--grey)}
.framed::after{content:"";position:absolute;right:0;bottom:-10px;width:44px;height:26px;border-bottom:6px solid var(--grey);border-right:6px solid var(--grey)}

/* about */
.about-photo-frame{position:absolute;left:112px;top:784px;width:382px;height:312px}
.about-photo-frame::before{content:"";position:absolute;left:0;top:0;width:190px;height:170px;border-top:6px solid var(--grey);border-left:6px solid var(--grey)}
.about-photo-frame::after{content:"";position:absolute;right:0;bottom:0;width:200px;height:170px;border-bottom:6px solid var(--grey);border-right:6px solid var(--grey)}
.about-photo{position:absolute;left:120px;top:795px;width:366px;height:291px;
  background:
    radial-gradient(ellipse 140px 90px at 150px 110px,rgba(210,210,210,.6) 0%,rgba(210,210,210,0) 100%),
    linear-gradient(180deg,#5a5a5a 0%,#3a3a3a 35%,#6b6b6b 60%,#2a2a2a 100%)}
.about-title{left:528px;top:790px;font-weight:900;font-size:30px}
.about-copy{position:absolute;left:528px;top:850px;width:552px;font-size:11.4px;line-height:19px;color:var(--ink)}
.btn{position:absolute;background:var(--white);border:1px solid var(--grey);font-weight:700;color:var(--ink);text-transform:uppercase;display:flex;align-items:center;justify-content:center}
.btn::before{content:"";position:absolute;left:-2px;top:-2px;width:24px;height:40px;border-top:4px solid var(--black);border-left:4px solid var(--black)}
.btn::after{content:"";position:absolute;right:-6px;bottom:-6px;width:54px;height:34px;border-bottom:4px solid var(--black);border-right:4px solid var(--black)}
.btn-read{left:526px;top:1050px;width:154px;height:42px;font-size:13px}

/* works */
.works{position:absolute;left:0;top:1188px;width:1200px;height:788px;background:var(--band)}
.works-title{left:478px;top:84px}
.grid{position:absolute;left:120px;top:170px;display:grid;grid-template-columns:repeat(4,232px);grid-template-rows:232px 232px;gap:10px 11px}
.tile{position:relative}
.t1{background:linear-gradient(45deg,#1b1b1b 0%,#777 30%,#ddd 45%,#555 60%,#222 100%)}
.t2{background:linear-gradient(180deg,rgba(0,0,0,.55),rgba(0,0,0,.7)),linear-gradient(135deg,#8a8a8a 0%,#4a4a4a 60%,#2a2a2a 100%);color:var(--white);text-align:center;padding:36px 18px 0}
.t3{background:radial-gradient(ellipse 70px 60px at 116px 140px,#e0e0e0 0%,rgba(150,150,150,0) 100%),linear-gradient(180deg,#111 0%,#2e2e2e 45%,#7a7a7a 75%,#b5b5b5 100%)}
.t4{background:radial-gradient(ellipse 120px 80px at 90px 190px,rgba(240,240,240,.75) 0%,rgba(240,240,240,0) 100%),linear-gradient(135deg,#5a5a5a 0%,#1b1b1b 45%,#3a3a3a 100%)}
.t5{background:radial-gradient(ellipse 80px 60px at 90px 70px,#f5f5f5 0%,rgba(120,120,120,.6) 50%,rgba(20,20,20,0) 100%),linear-gradient(180deg,#1a1a1a 0%,#0d0d0d 100%)}
.t6{background:linear-gradient(110deg,rgba(255,255,255,0) 40%,rgba(255,255,255,.35) 48%,rgba(255,255,255,0) 56%),linear-gradient(160deg,#6d6d6d 0%,#3a3a3a 50%,#1d1d1d 100%)}
.t7{background:linear-gradient(180deg,rgba(0,0,0,0) 55%,rgba(220,220,220,.35) 80%,rgba(0,0,0,.2) 100%),linear-gradient(90deg,#0d0d0d 0%,#3a3a3a 35%,#bdbdbd 50%,#3a3a3a 65%,#111 100%)}
.t8{background:radial-gradient(ellipse 90px 60px at 140px 170px,rgba(235,235,235,.7) 0%,rgba(235,235,235,0) 100%),radial-gradient(ellipse at 40% 25%,#8a8a8a 0%,#333 45%,#0f0f0f 100%)}
.tile-head{font-weight:700;font-size:16px;letter-spacing:.5px;padding-bottom:8px;border-bottom:2px solid var(--white);display:inline-block;margin-bottom:10px}
.tile-copy{font-size:10.4px;line-height:14px}
.tile-more{position:absolute;left:106px;top:184px;width:22px;height:22px}
.view-all{position:absolute;left:0;top:690px;width:1200px;text-align:center;font-weight:700;font-style:italic;font-size:16px}
.view-all a{color:var(--ink);text-decoration:underline}

/* contact */
.contact-title{left:486px;top:2076px}
.contact-copy{position:absolute;left:140px;top:2154px;width:920px;text-align:center;font-size:11.4px;line-height:22px}
.field{position:absolute;background:var(--paper);border:1px solid var(--band);font-size:12.5px;color:var(--ink);padding:8px 8px}
.f-name{left:120px;top:2232px;width:308px;height:36px}
.f-phone{left:446px;top:2232px;width:308px;height:36px}
.f-email{left:774px;top:2232px;width:306px;height:36px}
.f-msg{left:120px;top:2288px;width:960px;height:74px}
.btn-submit{left:522px;top:2394px;width:156px;height:42px;font-size:17px}

/* footer */
.footer{position:absolute;left:0;top:2511px;width:1200px;height:484px;color:var(--white);
  clip-path:polygon(0 101px,600px 0,1200px 101px,1200px 484px,0 484px);
  background:
    radial-gradient(ellipse 520px 110px at 600px 450px,rgba(110,110,110,.7) 0%,rgba(60,60,60,0) 100%),
    repeating-linear-gradient(90deg,rgba(0,0,0,0) 0,rgba(0,0,0,0) 238px,rgba(0,0,0,.25) 238px,rgba(0,0,0,.25) 240px),
    linear-gradient(180deg,#3a3a3a 0%,#262626 55%,#1b1b1b 100%)}
.info{position:absolute;top:94px;width:260px;text-align:center}
.info .icon{display:block;margin:0 auto 16px;width:62px;height:62px}
.info h3{font-size:14px;font-weight:700;text-transform:uppercase;margin-bottom:6px}
.info p{font-size:14px;color:var(--white)}
.i-loc{left:160px}
.i-phone{left:492px}
.i-mail{left:840px}
.footer .brand{left:0;width:1200px;justify-content:center;top:272px;font-size:38px;color:var(--white)}
.footer .brand .mark{width:24px;height:24px}
.foot-nav{position:absolute;top:364px;left:0;width:1200px;display:flex;justify-content:center;font-size:13.5px}
.foot-nav a{color:var(--white);text-decoration:none;padding:0 40px}
.foot-nav a+a{border-left:1px solid rgba(255,255,255,.4)}
.foot-rule{position:absolute;left:120px;top:416px;width:960px;height:1px;background:rgba(255,255,255,.2)}
.copyright{position:absolute;left:120px;top:446px;font-size:12px}
.social{position:absolute;left:914px;top:440px;display:flex;gap:14px}
.social span{width:30px;height:30px;border-radius:50%;border:2px solid var(--white)}
.social .s1{background:var(--social-a)}
.social .s2{background:var(--social-b)}
.social .s3{background:var(--social-c)}
.social .s4{background:var(--social-d)}
</style>
</head>
<body>

<header class="hero" role="img" aria-label="Black and white photo of a worker inside an underground construction site, light streaming down">
  <div class="brand"><span class="mark"></span>MOTOR VAULT</div>
  <nav class="nav">
    <a class="current">HOME</a><a>ABOUT US</a><a>OUR WORKS</a><a>CONTACT US</a>
  </nav>
  <h1 class="hero-title">We are car parks for private residential homes in London<br>and the influential counties within the UK</h1>
  <div class="dots"><span></span><span class="on"></span><span></span><span></span></div>
</header>

<section class="about">
  <div class="about-photo-frame"></div>
  <div class="about-photo" role="img" aria-label="Black and white photo of an excavated basement with workers and machinery"></div>
  <h2 class="section-title about-title">About Motor Vault</h2>
  <p class="about-copy">Motor Vault designs and builds bespoke subterranean car parks beneath private residential homes across London and the finest counties of the United Kingdom. Every project begins with a careful survey of the ground, the structure above and the way our clients live. Our engineers then shape a quiet, secure space that protects a collection and frees the street from parked cars. We handle planning, excavation, waterproofing, lighting, ventilation and lifts under one contract, so owners deal with a single team from first sketch to final handover. Finishes are chosen with the same care as the cars they hold, from polished concrete and stone to custom lighting and climate control. As part of the Brantley Group, we bring decades of experience to every site and every vault we build.</p>
  <a class="btn btn-read">Read More»</a>
</section>

<section class="works">
  <h2 class="section-title framed works-title">Our Works</h2>
  <div class="grid">
    <div class="tile t1" role="img" aria-label="Steel framework of an underground structure"></div>
    <div class="tile t2" role="img" aria-label="Excavation site photo behind project summary">
      <div class="tile-head">LOREM IPSUM</div>
      <p class="tile-copy">A private vault beneath a Kensington townhouse, built for six cars with a turntable, gallery lighting and a quiet lift to the garden above. Completed in 2018.</p>
      <svg class="tile-more" viewBox="0 0 22 22"><circle cx="11" cy="11" r="10" fill="none" stroke="#fff" stroke-width="1.5"/><path d="M9 6.5l4.5 4.5L9 15.5" fill="none" stroke="#fff" stroke-width="1.8"/></svg>
    </div>
    <div class="tile t3" role="img" aria-label="Empty concrete car park with columns"></div>
    <div class="tile t4" role="img" aria-label="Underground garage with a ribbed wall"></div>
    <div class="tile t5" role="img" aria-label="Bright work lights inside a dark excavation"></div>
    <div class="tile t6" role="img" aria-label="Worker in a beam of light on a building site"></div>
    <div class="tile t7" role="img" aria-label="Long concrete corridor with light falling between pillars"></div>
    <div class="tile t8" role="img" aria-label="Welder at work with sparks flying"></div>
  </div>
  <div class="view-all"><a>VIEW ALL »</a></div>
</section>

<section class="contact">
  <h2 class="section-title framed contact-title">Contact Us</h2>
  <p class="contact-copy">Tell us about your home and your collection. Share a few details below and a member of our team will arrange a private consultation at a time that suits you, in London or anywhere across the counties.</p>
  <div class="field f-name">Your Name</div>
  <div class="field f-phone">Phone</div>
  <div class="field f-email">Email</div>
  <div class="field f-msg">Message</div>
  <a class="btn btn-submit">Submit»</a>
</section>

<footer class="footer" role="img" aria-label="Dark concrete wall with a soft glow on the floor">
  <div class="info i-loc">
    <svg class="icon" viewBox="0 0 62 62"><circle cx="31" cy="31" r="31" fill="#fff"/><path d="M31 18c-5.5 0-9.5 4-9.5 9.3 0 6.7 9.5 16.7 9.5 16.7s9.5-10 9.5-16.7C40.5 22 36.5 18 31 18z" fill="#1b1b1b"/><circle cx="31" cy="27.5" r="3.4" fill="#fff"/></svg>
    <h3>Motor Vault</h3>
    <p>22 Harlow Yard, London, W9 4QT</p>
  </div>
  <div class="info i-phone">
    <svg class="icon" viewBox="0 0 62 62"><circle cx="31" cy="31" r="31" fill="#fff"/><path d="M23.5 18.5l4.5-1 3 7-3 2.2c1.5 3.4 4 6 7.3 7.5l2.3-3 7 3-1 4.6c-.4 1.4-1.6 2.2-3 2.2C29.8 41 21 32.2 21 21.4c0-1.4 1-2.6 2.5-2.9z" fill="#1b1b1b"/></svg>
    <h3>Phone</h3>
    <p>0207 555 0142</p>
  </div>
  <div class="info i-mail">
    <svg class="icon" viewBox="0 0 62 62"><circle cx="31" cy="31" r="31" fill="#fff"/><rect x="19" y="22" width="24" height="17" fill="#1b1b1b"/><path d="M19.5 22.5L31 32l11.5-9.5" fill="none" stroke="#fff" stroke-width="1.6"/></svg>
    <h3>Email</h3>
    <p>info@motorvault.example</p>
  </div>
  <div class="brand"><span class="mark"></span>MOTOR VAULT</div>
  <nav class="foot-nav"><a>HOME</a><a>ABOUT US</a><a>OUR WORKS</a><a>CONTACT US</a></nav>
  <div class="foot-rule"></div>
  <p class="copyright">Copyright © 2019 MOTOR VAULT . All Right Reserved.</p>
  <div class="social"><span class="s1"></span><span class="s2"></span><span class="s3"></span><span class="s4"></span></div>
</footer>

</body>
</html>
```